Accountability Project Graphics

I want to create 10 social media graphics (new Instagram size 4:5 (1080 x 1350 pixels) focusing on our Quenral Accountability App, using any of the 3 pictures attached. Use the attached pics only, NO RANDOM STOCK PHOTOGRAPHY. For the color scheme, use the landing page colors/fonts (attached).
You can add any of the 3 photos attached but I mainly need BOLD text that includes these headlines and sub-headlines on them.
Please NOTE for all the headlines below, also add this sub-headline on each graphic:
Stay Consistent with RB in Your Pocket!
Here are the headlines:
• Stop Starting Over Every Monday
• You don't need more willpower. You need more support
• Built for women who are tired of doing this alone
• When Motivation Fades, RB Checks In
• The Support System You've Been Missing
• Support When Motivation Disappears
• What if RB Checked in Every Day?
• The Missing Piece Isn't Another Diet
• Eat the food you love. Stay accountable every day.
• One Bad Meal Doesn't Mean You Failed
Target Market(s)
women over 40 trying to lose weight
Look and feel
Each slider illustrates characteristics of the customer's brand and the style your logo design should communicate.

```html
<!DOCTYPE html>
<html lang="en">
<head>
<meta charset="utf-8">
<title>Quenral Accountability App – Social Graphics</title>
<link rel="stylesheet" href="https://fonts.googleapis.com/css2?family=Playfair+Display:ital,wght@0,700;0,900;1,700;1,900&family=Roboto:ital,wght@0,700;1,700&display=swap">
<style>
:root{
  --canvas:#6b6b6b;
  --plum:#2b1436;
  --plum-deep:#3d1740;
  --rose:#c65a7e;
  --rose-soft:#d98aa6;
  --blush:#f8e2ea;
  --blush-light:#fbf1f4;
  --white:#ffffff;
  --photo-a:#c9a9b4;
  --photo-b:#3a3346;
}
*{margin:0;padding:0;box-sizing:border-box}
html,body{width:1200px;height:3484px;overflow:hidden;background:var(--canvas)}
body{position:relative;font-family:'Playfair Display',Georgia,serif}
.card{position:absolute;width:494px;height:617px;overflow:hidden;background:linear-gradient(180deg,var(--blush) 0%,var(--blush-light) 100%)}
.col-l{left:88px}.col-r{left:630px}
.row1{top:107px}.row2{top:766px}.row3{top:1425px}.row4{top:2084px}.row5{top:2743px}
.abs{position:absolute}
.head{font-weight:900;color:var(--plum);line-height:1}
.pink{color:var(--rose)}
.it{font-style:italic}
.center{text-align:center}
.photo{position:absolute;background:linear-gradient(160deg,var(--photo-a) 0%,var(--photo-b) 100%)}
.photo.soft{background:radial-gradient(ellipse at 50% 40%,var(--photo-a) 0%,#8d6f86 55%,var(--blush) 100%)}
.tag{font-family:'Roboto',Arial,sans-serif;font-weight:700;color:var(--white)}
.tag em{color:var(--rose-soft)}
.band-dark{position:absolute;left:0;right:0;bottom:0;height:47px;background:linear-gradient(90deg,var(--plum) 0%,var(--plum-deep) 100%);display:flex;align-items:center;justify-content:center;font-size:22px;font-style:italic}
</style>
</head>
<body>

<!-- 1 -->
<section class="card col-l row1">
  <div class="photo" role="img" aria-label="Smiling woman in a black outfit, hand on hip" style="left:320px;top:20px;width:174px;height:425px;border-radius:80px 80px 0 0"></div>
  <div class="abs head" style="left:26px;top:58px;font-size:64px;line-height:74px">Stop<br>Starting<br>Over</div>
  <div class="abs head pink it" style="left:24px;top:284px;font-size:64px;line-height:74px">Every<br>Monday</div>
  <div class="abs tag center" style="left:0;right:0;top:445px;height:172px;background:var(--rose);display:flex;flex-direction:column;justify-content:center;font-size:33px;line-height:44px">
    <span>Stay Consistent with</span><span class="it">RB in Your Pocket!</span></div>
</section>

<!-- 2 -->
<section class="card col-r row1">
  <div class="photo soft" role="img" aria-label="Two women embracing and laughing" style="left:100px;top:270px;width:320px;height:300px;border-radius:50%"></div>
  <div class="abs head pink" style="left:22px;top:50px;font-size:46px;line-height:70px;font-weight:700">You<br>don't<br>need<br>more<br><span class="it">will<br>power.</span></div>
  <div class="abs head right" style="right:32px;top:28px;font-size:52px;line-height:54px;text-align:right">You<br>need<br>More</div>
  <div class="abs head it" style="right:30px;top:186px;font-size:52px;line-height:54px;width:44px;text-align:center">S<br>u<br>p<br>p<br>o<br>r<br>t</div>
  <div class="band-dark tag">Stay Consistent with&nbsp;<em>RB in Your Pocket!</em></div>
</section>

<!-- 3 -->
<section class="card col-l row2">
  <div class="abs head center" style="left:0;right:0;top:48px;font-size:92px">Built for</div>
  <div class="abs head center it" style="left:0;right:0;top:122px;font-size:84px">women</div>
  <div class="abs pink it center" style="left:0;right:0;top:216px;font-size:28px;font-weight:700">who are tired of doing this alone</div>
  <div class="photo soft" role="img" aria-label="Two women standing together, laughing" style="left:100px;top:270px;width:310px;height:300px"></div>
  <div class="band-dark tag">Stay Consistent with&nbsp;<em>RB in Your Pocket!</em></div>
</section>

<!-- 4 -->
<section class="card col-r row2">
  <div class="photo soft" role="img" aria-label="Smiling woman in a black outfit, hand on hip" style="left:90px;top:15px;width:320px;height:602px"></div>
  <div class="abs center" style="left:16px;width:462px;top:310px;height:290px;background:rgba(198,90,126,.85);border-radius:12px">
    <div class="it" style="margin-top:24px;font-size:32px;font-weight:700;color:var(--white)">When Motivation Fades,</div>
    <div class="it" style="font-size:86px;font-weight:900;color:var(--white);line-height:.95">RB</div>
    <div style="font-size:68px;font-weight:900;color:var(--white);line-height:1.05">Checks In</div>
    <div class="tag it" style="font-size:24px;margin-top:14px">Stay Consistent with RB in Your Pocket!</div>
  </div>
</section>

<!-- 5 -->
<section class="card col-l row3">
  <div class="abs" style="left:10px;top:14px;width:474px;height:419px;border:3px solid var(--rose);border-radius:26px;box-shadow:inset 0 0 0 4px var(--blush),inset 0 0 0 5px var(--rose)"></div>
  <div class="abs head center" style="left:0;right:0;top:46px;font-size:94px">The</div>
  <div class="abs head center pink" style="left:0;right:0;top:138px;font-size:94px">Support</div>
  <div class="abs head center" style="left:0;right:0;top:236px;font-size:94px">System</div>
  <div class="abs pink it center" style="left:0;right:0;top:340px;font-size:44px;font-weight:700">You've Been Missing</div>
  <div class="abs tag center" style="left:0;right:0;top:488px;font-size:35px;line-height:44px;color:var(--plum)">Stay Consistent with<br><span style="color:var(--rose)">RB in Your Pocket!</span></div>
</section>

<!-- 6 -->
<section class="card col-r row3">
  <div class="abs head center" style="left:0;right:0;top:32px;font-size:96px">Support</div>
  <div class="abs pink it center head" style="left:0;right:0;top:132px;font-size:48px;line-height:70px">When Motivation<br>Disappears</div>
  <div class="photo soft" role="img" aria-label="Two women standing together, laughing" style="left:70px;top:270px;width:350px;height:310px"></div>
  <div class="abs tag center" style="left:52px;width:390px;bottom:0;height:106px;background:var(--rose);border-radius:50px 50px 0 0;font-size:32px;line-height:40px;padding-top:14px">Stay&nbsp; Consistent with<br>RB in Your Pocket!</div>
</section>

<!-- 7 -->
<section class="card col-l row4">
  <div class="photo" role="img" aria-label="Smiling woman in a black outfit, hand on hip" style="left:320px;top:170px;width:174px;height:447px;border-radius:80px 80px 0 0"></div>
  <div class="abs head" style="left:18px;top:44px;font-size:74px">What if</div>
  <div class="abs head pink it" style="left:14px;top:110px;font-size:150px">RB</div>
  <div class="abs head pink" style="left:20px;top:268px;font-size:44px">Checked in</div>
  <div class="abs head" style="left:18px;top:322px;font-size:96px;line-height:92px">Every<br>Day?</div>
  <div class="abs tag" style="left:0;width:355px;top:522px;height:95px;background:var(--rose);font-size:30px;line-height:38px;padding:10px 0 0 26px">Stay&nbsp; Consistent with<br>RB in Your Pocket!</div>
</section>

<!-- 8 -->
<section class="card col-r row4">
  <svg class="abs" style="left:0;top:0" width="494" height="617" aria-hidden="true">
    <polygon points="340,0 494,0 494,200" fill="var(--plum)"/>
    <polygon points="0,440 0,617 160,617" fill="var(--plum)"/>
    <rect x="22" y="20" width="450" height="577" fill="none" stroke="var(--rose)" stroke-width="2"/>
  </svg>
  <div class="abs head center" style="left:0;right:0;top:76px;font-size:58px">The</div>
  <div class="abs head center pink it" style="left:0;right:0;top:156px;font-size:58px">Missing Piece</div>
  <div class="abs head center" style="left:0;right:0;top:236px;font-size:58px">Isn't</div>
  <div class="abs head center it" style="left:0;right:0;top:316px;font-size:58px">Another Diet</div>
  <div class="abs tag center" style="left:40px;width:414px;top:434px;height:142px;background:var(--rose);display:flex;flex-direction:column;justify-content:center;font-size:37px;line-height:48px"><span>Stay Consistent with</span><span class="it">RB in Your Pocket!</span></div>
</section>

<!-- 9 -->
<section class="card col-l row5">
  <div class="abs head center pink" style="left:0;right:0;top:38px;font-size:70px;line-height:76px">Eat the food<br>you love.</div>
  <div class="abs head center it" style="left:0;right:0;top:196px;font-size:70px">Stay</div>
  <div class="abs head center it" style="left:0;right:0;top:270px;font-size:68px">Accountable</div>
  <div class="abs head center it pink" style="left:0;right:0;top:336px;font-size:64px">Every day</div>
  <div class="abs" style="left:18px;width:458px;top:460px;height:143px;background:var(--rose)">
    <div class="tag center" style="margin-top:20px;font-size:31px">Stay Consistent with</div>
    <div class="tag center it" style="margin:10px auto 0;width:380px;height:44px;line-height:44px;border-radius:22px;background:var(--plum);font-size:30px">RB in Your Pocket!</div>
  </div>
</section>

<!-- 10 -->
<section class="card col-r row5">
  <div class="abs center" style="left:30px;width:434px;top:26px;height:350px;background:var(--rose-soft)"></div>
  <div class="abs head center it" style="left:0;right:0;top:52px;font-size:52px;color:var(--white)">One Bad Meal</div>
  <div class="abs head center" style="left:0;right:0;top:132px;font-size:50px;color:var(--white)">Doesn't Mean</div>
  <div class="abs head center" style="left:0;right:0;top:208px;font-size:52px;color:var(--white)">You Failed</div>
  <div class="photo soft" role="img" aria-label="Two women standing together, laughing" style="left:80px;top:290px;width:340px;height:282px"></div>
  <div class="band-dark tag">Stay Consistent with&nbsp;<em>RB in Your Pocket!</em></div>
</section>

</body>
</html>
```